Inclusive life skills courses upskilling in wellbeing, academic success and career readines

I need a web design that is corporate and engaging. It needs to capture what we do and our core course offering. We develop courses and make customised course provision that cultivate 21st-century competencies that support academic achievement and social and emotional skills fostering personal growth and academic skill development that are relevant and timely for the learner. This prepares them for present and future challenges and opportunities, while contributing to students’ career portfolio with an accredited, relevant and adaptive provision. Our initial course is a Level 1 course. Here are the tentative course details. The courses will be accessed through the site, it should be crisp, clear and simple.

Level 1 Grounded Growth Journey is part of the GVDM designed to equip students with essential life skills. Accredited and focused on social-emotional learning, academic skills, and work preparation, this program offers a comprehensive approach to student development.

Course Structure
Certificates: Six short courses (micro learning) each can be taken individually or as a whole offering.
Credit Integration: Completing all six courses cumulates credits.
Course Duration: Each course involves 3 hours of content, 6 hours of practical application, and 3 hours of portfolio work and reflection.
*Note REFO Tariff is possible with BTK L3. An accredited CPD course may be simpler.
Short Courses within Level 1 GVDM
Self-Awareness: A sense of purpose. understand emotions, thoughts, and values and how they influence behavior across contexts. This includes capacities to recognize one’s strengths and limitations with a well- grounded sense of confidence and purpose.
Self-Management: A sense of self. Manage emotions, and behaviors in different situations to achieve goals and aspirations while managing time, stress and balance.
Building Resilience: Overcome challenges and adversity. Develop the confidence to face life’s challenges and reach your full potential, feeling more capable and in control of your life
Motivation & Mindset: Cultivating a positive approach and drive. This requires effective study skills, a growth mindset, gratitude and techniques to find work life balance.
Communication: Build rapport. Approach different types of conversation with confidence and clarity, listen and relate to others and manage requests.
Making an Impact: Develop assertiveness and confidence. Confidently share your ideas and opinions, improve your influencing skills and explore the trust equation.
Skills badges in progress: problem-solving, leadership, teamwork, listening, aiming high, staying positive.
Approach
Student-Centric: Courses blend digital learning with practical application.
Flexibility: Self-paced, adaptable to independent or classroom learning.
Digital Integration: Includes digital portfolio of practice (DPP) and skill bite certificates.
Practical Application: Emphasizes real-world skills and portfolio building.
Progress monitoring: Students are empowered in their learning and development.
Customization: AI-driven to tailor courses to student needs.
Aim and Impact
This qualification is designed to be directly relevant and applicable to students’ daily lives, encouraging personal growth and skill development. It’s a flexible offering, which is self-paced or blended (flipped) with the practical components integrated into classes. Teachers and students experience flipped learning and then practice and develop portfolio through subject teaching.

Progression Levels (BTK or CPD)

Level 1 Training for Life and Work (CPD Credits)
Level 2 Project Management and Teamwork (CPD Credits)
Level 3 Leading, Mentoring, Coaching
Level 4 Innovative Entrepreneurship

Please note: A logo will be available. The colour branding is similar to this:https://tavorlane.com/ and this: https://brimquell.com/

Education (K-12, university and corporate)

1 page

Serif

0054AA
0677BA
7BADD7
CADEEF
E8F1F8
0094D4
00A9DD
6FCCEA
C7EBF8
E9F6FB
00AB8E
00BBA5
67D7C9
C6EFE9
E9F9F6

• Simple, captures what we do.

```html
<!DOCTYPE html>
<html lang="en">
<head>
<meta charset="utf-8">
<title>Let's Learn about new Knowledge and abilities</title>
<link href="https://fonts.googleapis.com/css2?family=Be+Vietnam+Pro:wght@400;500;700&display=swap" rel="stylesheet">
<style>
  :root {
    --ink: #0c0c3a;
    --text: #2a2a33;
    --muted: #6c6f78;
    --orange: #ff9500;
    --blue: #0054aa;
    --bg-top: #ffffff;
    --bg-bottom: #edf1f5;
    --photo-a: #e0a73a;
    --photo-b: #c98d26;
    --photo-c: #d9d5cc;
  }
  * { box-sizing: border-box; margin: 0; padding: 0; }
  html, body { width: 1200px; height: 708px; overflow: hidden; }
  body {
    font-family: "Be Vietnam Pro", sans-serif;
    background: linear-gradient(180deg, var(--bg-top) 0%, var(--bg-bottom) 100%);
    position: relative;
    color: var(--text);
  }
  .site-header {
    position: absolute; left: 67px; right: 67px; top: 17px; height: 44px;
    display: flex; align-items: center;
  }
  .brand { display: flex; align-items: center; gap: 9px; text-decoration: none; }
  .brand-dot { width: 37px; height: 37px; border-radius: 50%; background: var(--orange); }
  .brand-name { color: var(--orange); font-weight: 700; font-size: 16px; }
  .main-nav {
    position: absolute; left: 349px; display: flex; gap: 30px;
  }
  .main-nav a, .sign-up {
    color: var(--text); text-decoration: none; font-size: 13.5px; font-weight: 400;
  }
  .account { margin-left: auto; display: flex; align-items: center; gap: 26px; }
  .login-btn {
    width: 93px; height: 43px; border-radius: 5px; background: var(--orange);
    color: #fff; font-size: 13.5px; display: flex; align-items: center; justify-content: center;
    text-decoration: none;
  }
  .hero-copy { position: absolute; left: 67px; top: 182px; width: 460px; }
  .hero-title {
    font-size: 53px; font-weight: 700; line-height: 70px; color: var(--ink);
    letter-spacing: 0.2px;
  }
  .highlight { position: relative; }
  .highlight-stroke { position: absolute; left: 3px; bottom: -13px; width: 268px; height: 12px; }
  .hero-lead {
    margin-top: 28px; width: 435px; font-size: 15px; line-height: 29px; color: var(--muted);
  }
  .enrol-btn {
    display: inline-flex; align-items: center; justify-content: center;
    margin-top: 35px; width: 135px; height: 45px; border-radius: 23px;
    background: var(--blue); color: #fff; font-weight: 700; font-size: 13.5px; text-decoration: none;
  }
  .hero-media {
    position: absolute; left: 627px; top: 162px; width: 504px; height: 441px;
    border-radius: 8px; overflow: hidden;
    background: linear-gradient(180deg, var(--photo-a) 0%, var(--photo-b) 70%, var(--photo-c) 100%);
  }
  .play-btn {
    position: absolute; left: 217px; top: 185px; width: 70px; height: 70px;
    border-radius: 50%; background: rgba(255,255,255,0.25);
    border: 2px solid rgba(255,255,255,0.35);
    display: flex; align-items: center; justify-content: center;
  }
</style>
</head>
<body>
  <header class="site-header">
    <a class="brand" href="#"><span class="brand-dot"></span><span class="brand-name">Logo Design</span></a>
    <nav class="main-nav">
      <a href="#">Home</a><a href="#">Courses</a><a href="#">About Us</a><a href="#">Pricing</a><a href="#">Contact</a>
    </nav>
    <div class="account">
      <a class="sign-up" href="#">Sign Up</a>
      <a class="login-btn" href="#">Login</a>
    </div>
  </header>

  <section class="hero-copy">
    <h1 class="hero-title">Let’s Learn about<br>new <span class="highlight">Knowledge<svg class="highlight-stroke" viewBox="0 0 268 12" aria-hidden="true"><path d="M2 10 Q134 -2 266 8" fill="none" stroke="#0054aa" stroke-width="3.5" stroke-linecap="round"/></svg></span><br>and abilities.</h1>
    <p class="hero-lead">We have created materials on various things that will help your career, with mentors who are experienced in their fields.</p>
    <a class="enrol-btn" href="#">Enrol Now</a>
  </section>

  <div class="hero-media" role="img" aria-label="Photo of two learners at a desk looking at a phone together against a yellow wall">
    <div class="play-btn">
      <svg width="26" height="30" viewBox="0 0 26 30" aria-hidden="true"><path d="M3 2 L24 15 L3 28 Z" fill="#fff" stroke="#fff" stroke-width="3" stroke-linejoin="round"/></svg>
    </div>
  </div>
</body>
</html>
```